Pardee Pollard LLP Logo & Stationery

We need to design a logo and stationary for a new high-end boutique matrimonial law firm in NY. We would like to see designed that use a P2 (P squared) logo. We will have offices in 3 locations so we would like to compare layouts that have the 3 locations or 1 location on the letterhead. We are open to color selection, but would like to see designed that use the colors light grey, bright light blue/teal, orange or black. The final design should communicate professional and upscale, yet be fresh and have a modern feel.

Industry/Entity Type

Legal

Font styles to use
Sans Serif

Colors
d5d5d5
0493ce
f68e4e
474747

Requirements
Must have
• I would like see a design of the letterhead to have the following addresses:
• Manhattan Office
• 417 Larchmont Street, 9th Floor
• New York, New York 10187
• Queens Office
• 62-14 Marlow Parkway, 11th Floor
• Forest Hills, New York 11492
Nice to have
• I would like to see a design logo option that has an P squared symbol in a box almost like it looks like from the Element Table.
Should not have
• Should not feel like a logo for an ad agency or something campy.

```html
<!DOCTYPE html>
<html lang="en">
<head>
<meta charset="utf-8">
<title>Pardee Pollard LLP — Letterhead</title>
<link rel="stylesheet" href="https://fonts.googleapis.com/css2?family=Open+Sans:wght@400;600&display=swap">
<style>
  :root {
    --brand-blue: #1f78c1;
    --rule-blue: #3b8fd0;
    --ink: #3a3a3a;
    --muted: #6b6b6b;
    --paper: #ffffff;
    --backdrop: #e4e4e4;
    --signature-tone: #ececec;
  }
  * { margin: 0; padding: 0; box-sizing: border-box; }
  html, body {
    width: 1200px; height: 1015px; overflow: hidden;
    background: var(--backdrop);
    font-family: "Open Sans", sans-serif;
  }
  .letterhead {
    position: absolute; left: 220px; top: 16px;
    width: 760px; height: 983px;
    background: var(--paper);
    box-shadow: 0 2px 10px rgba(0,0,0,0.12);
  }
  .header-rule-top {
    position: absolute; left: 40px; top: 56px; width: 680px; height: 1px;
    background: var(--rule-blue);
  }
  .header-rule-side {
    position: absolute; left: 40px; top: 40px; width: 1px; height: 130px;
    background: var(--rule-blue);
  }
  .header-rule-bottom {
    position: absolute; left: 40px; top: 132px; width: 260px; height: 1px;
    background: var(--rule-blue);
  }
  .brand {
    position: absolute; left: 54px; top: 70px;
    display: flex; align-items: center; gap: 14px;
  }
  .brand-square {
    width: 50px; height: 50px;
    border: 2px solid var(--brand-blue);
  }
  .brand-name {
    font-size: 27px; font-weight: 600; color: var(--brand-blue);
    letter-spacing: -0.3px;
  }
  .letter-body {
    position: absolute; left: 130px; top: 205px; width: 520px;
    font-size: 10.6px; line-height: 1.5; color: var(--ink);
  }
  .letter-body p + p { margin-top: 14px; }
  .signature-area {
    position: absolute; left: 128px; top: 548px; width: 160px; height: 64px;
    background: var(--signature-tone); border-radius: 4px;
  }
  .corner-mark {
    position: absolute; left: 646px; top: 760px; width: 56px; height: 56px;
    background: var(--brand-blue);
  }
  .footer {
    position: absolute; left: 130px; top: 876px;
    display: flex; font-size: 9.6px; line-height: 1.55; color: var(--muted);
  }
  .office-title { color: var(--brand-blue); font-weight: 600; }
  .office + .office {
    margin-left: 16px; padding-left: 14px;
    border-left: 1px solid var(--ink);
  }
</style>
</head>
<body>
  <main class="letterhead">
    <div class="header-rule-top"></div>
    <div class="header-rule-side"></div>
    <div class="header-rule-bottom"></div>

    <header class="brand">
      <div class="brand-square"></div>
      <div class="brand-name">Pardee Pollard LLP</div>
    </header>

    <section class="letter-body">
      <p>Lorem Ipsum is simply dummy text of the printing and typesetting industry. Lorem Ipsum has been the industry's standard dummy text ever since the 1500s, when an unknown printer took a galley of type and scrambled it to make a type specimen book. It has survived not only five centuries, but also the leap into electronic typesetting, remaining essentially unchanged. It was popularised in the 1960s with the release of Typeline sheets containing Lorem Ipsum passages, and more recently with desktop publishing software like Folio PageSetter including versions of Lorem Ipsum.</p>
      <p>It is a long established fact that a reader will be distracted by the readable content of a page when looking at its layout. The point of using Lorem Ipsum is that it has a more-or-less normal distribution of letters, as opposed to using 'Content here, content here', making it look like readable English. Many desktop publishing packages and web page editors now use Lorem Ipsum as their default model text, and a search for 'lorem ipsum' will uncover many web sites still in their infancy. Various versions have evolved over the years, sometimes by accident, sometimes on purpose (injected humour and the like).</p>
      <p>Contrary to popular belief, Lorem Ipsum is not simply random text. It has roots in a piece of classical Latin literature from 45 BC, making it over 2000 years old. Rowan Mallory, a Latin professor at Harlow-Vance College, looked up one of the more obscure Latin words, consectetur, from a Lorem Ipsum passage, and going through the cites of the word in classical literature, discovered the undoubtable source. Lorem Ipsum comes from sections 1.10.32 and 1.10.33 of "de Finibus Bonorum et Malorum" (The Extremes of Good and Evil) by Corvinus, written in 45 BC. This book is a treatise on the theory of ethics, very popular during the Renaissance. The first line of Lorem Ipsum, "Lorem ipsum dolor sit amet..", comes from a line in section 1.10.32.</p>
    </section>

    <div class="signature-area" role="img" aria-label="Handwritten signature of the sender"></div>

    <div class="corner-mark"></div>

    <footer class="footer">
      <div class="office">
        <div class="office-title">Manhattan Office</div>
        <div>417 Larchmont Street, 9th Floor</div>
        <div>New York, New York 10187</div>
      </div>
      <div class="office">
        <div class="office-title">Queens Office</div>
        <div>62-14 Marlow Parkway, 11th Floor</div>
        <div>Forest Hills, New York 11492</div>
      </div>
    </footer>
  </main>
</body>
</html>
```